Veteran Owned General Contractor needs Bold New Business Cards

We are a service disabled veteran owned small business. We're a general contractor that specializes in excavation, underground utilities, site work, land clearing and demolition. We would like a fresh, simple, bold, new look for our business cards. We're open to ideas! We'd like to incorporate the following information on the card:

Company Name & Logo, Name of Person, Job Title, Office Phone, Fax, Cell Phone, Email Address, Website, SDVOSB

Our logo is included. We look forward to your thoughts.

Thank you!
Updates

Reason: Hello Due to the overwhelming response to this project, we are extending the deadline one time to allow for improved communication and feedback with the top candidates. We would like to thank everyone for their hard work and exceptional creativity! Thank you

Industry/Entity Type

Business

Contact Information for Business Card

Font styles to use
Sans Serif

Requirements
Nice to have
• As we are a veteran owned company, it would be nice to incorporate an American flag into the design. Maybe on the back?

```html
<!DOCTYPE html>
<html lang="en">
<head>
<meta charset="utf-8">
<title>Ridgeline Works – Business Card</title>
<link href="https://fonts.googleapis.com/css2?family=Lato:wght@400;700;900&display=swap" rel="stylesheet">
<style>
  :root{
    --green:#6cbf3f;
    --ink:#3a3a3a;
    --card:#f4f4f4;
    --bg:#2b2b2b;
    --mark:#2e2e2e;
    --flag-red:#c0273d;
    --flag-white:#ffffff;
    --flag-blue:#3c3b6e;
  }
  html,body{margin:0;height:100%;overflow:hidden}
  body{
    width:1200px;height:834px;background:var(--bg);
    font-family:"Lato",sans-serif;position:relative;
  }
  .card{
    position:absolute;left:320px;width:560px;height:320px;
    background:linear-gradient(135deg,#ffffff 0%,var(--card) 60%,#e9e9e9 100%);
    overflow:hidden;box-shadow:0 10px 30px rgba(0,0,0,.45);
  }
  .card--front{top:56px}
  .card--back{top:458px}

  .brand{position:absolute;display:flex;align-items:center;gap:10px}
  .brand__square{width:34px;height:34px;background:var(--mark);border-radius:6px}
  .brand__name{font-weight:900;color:var(--green);font-size:30px;letter-spacing:1px;white-space:nowrap}

  .card--front .brand{left:72px;top:118px}
  .flag{position:absolute;left:448px;top:78px;width:70px;height:38px;display:block}
  .band{position:absolute;left:0;right:0;top:212px;height:34px;background:var(--green);
    display:flex;align-items:center;justify-content:center}
  .band__url{color:#fff;font-size:13px;letter-spacing:.3px}

  .card--back .brand{right:34px;top:40px}
  .card--back .brand__square{width:28px;height:28px;border-radius:5px}
  .card--back .brand__name{font-size:24px}

  .contacts{position:absolute;right:30px;top:118px;list-style:none;margin:0;padding:0;
    font-size:13px;color:var(--ink);text-align:right;line-height:19px}
  .contacts li{display:flex;justify-content:flex-end;align-items:center;gap:10px}
  .contacts svg{width:11px;height:11px;stroke:var(--green);fill:none;stroke-width:1.6}

  .accent{position:absolute;left:-16px;top:178px;width:32px;height:32px;border-radius:50%;background:var(--green)}
  .person{position:absolute;left:34px;top:168px}
  .person__name{margin:0;font-size:20px;font-weight:700;color:var(--ink)}
  .person__role{margin:2px 0 0;font-size:16px;color:var(--green)}
  .address{position:absolute;left:34px;bottom:30px;font-size:13px;color:var(--ink);line-height:18px;font-style:normal}
</style>
</head>
<body>

<section class="card card--front">
  <div class="brand">
    <span class="brand__square"></span>
    <span class="brand__name">RIDGELINE WORKS</span>
  </div>
  <svg class="flag" viewBox="0 0 70 38" role="img" aria-label="American flag">
    <rect width="70" height="38" fill="var(--flag-white)"/>
    <g fill="var(--flag-red)">
      <rect y="0" width="70" height="2.92"/>
      <rect y="5.85" width="70" height="2.92"/>
      <rect y="11.7" width="70" height="2.92"/>
      <rect y="17.54" width="70" height="2.92"/>
      <rect y="23.38" width="70" height="2.92"/>
      <rect y="29.23" width="70" height="2.92"/>
      <rect y="35.08" width="70" height="2.92"/>
    </g>
    <rect width="28" height="20.46" fill="var(--flag-blue)"/>
  </svg>
  <div class="band"><span class="band__url">www.ridgelineworks.com</span></div>
</section>

<section class="card card--back">
  <div class="brand">
    <span class="brand__square"></span>
    <span class="brand__name">RIDGELINE WORKS</span>
  </div>

  <ul class="contacts">
    <li>+1 555 014 2290
      <svg viewBox="0 0 12 12"><rect x="3" y="1" width="6" height="10" rx="1"/></svg></li>
    <li>+1 555 014 2291
      <svg viewBox="0 0 12 12"><path d="M1 5c2-3 8-3 10 0l-2 1-1-1H4L3 6z"/><rect x="3" y="7" width="6" height="4"/></svg></li>
    <li>+1 555 014 2292
      <svg viewBox="0 0 12 12"><rect x="3" y="1" width="6" height="3"/><rect x="1" y="4" width="10" height="5"/><rect x="3" y="8" width="6" height="3"/></svg></li>
    <li>dan@ridgeline.com
      <svg viewBox="0 0 12 12"><rect x="1" y="2.5" width="10" height="7"/><path d="M1 2.5l5 4 5-4"/></svg></li>
  </ul>

  <span class="accent"></span>
  <div class="person">
    <h2 class="person__name">Dan Mercer</h2>
    <p class="person__role">Founder</p>
  </div>
  <address class="address">Via Lario, 14<br>20150 - Comasco (VA)</address>
</section>

</body>
</html>
```